Quillmark 5.2 - Educational Guide/Course-pack/Worksheet

Our Quillmark 5.2 toolkit is an educational workshop that focuses on inspiring student initiatives in the classroom! We need a new educational course guide or course-pack for students/teachers that clearly outlines or explains the program steps, offers helpful tips and includes empty spaces/lines where their can write down their great ideas or notes. This will include a;

- Teachers Guide (1 Page)
- Student Guide/Worksheet (4 Pages)
- Group Pack Resources (3 Pages)

This will consist of designing/formatting text, stock animation/icons, font, etc. We have included our new logo (color, branding, etc.) and all of the text for each separate course-pack. We have also attached our new website to give you an idea of the program style.

Our workshop can be for any school project like Technology, Community, Environment, Art, Science, etc.

Target Market(s)

High School Students/Teachers

Industry/Entity Type

Education

Font styles to use
Sans Serif

Colors
f68e4e
acd037
34a7d8

Requirements
Must have
• Use our brand colors from logo.
Should not have
• Should not be too childish.

```html
<!DOCTYPE html>
<html lang="en">
<head>
<meta charset="utf-8">
<title>Quillmark 5.2 – Launch the Project</title>
<link href="https://fonts.googleapis.com/css2?family=Roboto:wght@400;500;700&display=swap" rel="stylesheet">
<style>
  :root{
    --orange:#f7a229;
    --coral:#f68e4e;
    --green:#acd037;
    --blue:#34a7d8;
    --blue-deep:#0089a8;
    --tag-text:#00a3cf;
    --tag-border:#7fc3e3;
    --ink:#333333;
    --muted:#9a9a9a;
    --paper:#ffffff;
  }
  *{margin:0;padding:0;box-sizing:border-box}
  html,body{width:849px;height:1200px;overflow:hidden;background:var(--paper)}
  body{font-family:"Roboto",Arial,sans-serif;color:var(--ink);position:relative}
  .sheet{position:relative;width:849px;height:1200px}

  .step-banner{position:absolute;left:76px;top:30px;width:422px;height:79px;border-radius:40px;
    background:linear-gradient(90deg,var(--blue-deep) 0%,#00a6cf 100%);overflow:hidden}
  .step-badge{position:absolute;left:0;top:0;width:96px;height:79px;border-radius:40px 0 0 40px;
    background:linear-gradient(135deg,var(--blue) 0%,var(--green) 55%,var(--coral) 100%)}
  .step-badge::after{content:"";position:absolute;left:14px;top:10px;width:58px;height:58px;border-radius:50%;background:var(--paper)}
  .step-number{position:absolute;left:14px;top:10px;width:58px;height:58px;z-index:1;
    display:flex;align-items:center;justify-content:center;font-weight:700;font-size:30px;color:var(--orange)}
  .step-title{position:absolute;left:122px;top:19px;font-weight:500;font-size:29px;letter-spacing:2.2px;color:#fff}

  .tag{position:absolute;left:77px;height:33px;padding:0 14px;border:3px solid var(--tag-border);border-radius:17px;
    font-weight:700;font-size:18px;line-height:27px;color:var(--tag-text)}

  .intro{position:absolute;left:91px;top:178px;font-weight:500;font-size:16.4px;line-height:25px}
  .intro ul{list-style:none;margin-left:-1px}
  .intro li{position:relative;padding-left:22px}
  .intro li::before{content:"";position:absolute;left:0;top:7px;width:11px;height:11px;border-radius:50%;background:#6fb9db}

  .role{position:absolute;left:76px;width:720px}
  .role-icon{position:absolute;left:0;top:0;width:66px;height:66px}
  .role-head{position:absolute;left:77px;top:0;white-space:nowrap;font-weight:700;font-size:17.5px}
  .role-name{color:var(--orange);letter-spacing:.3px;margin-right:14px}
  .role-area{color:var(--muted);font-size:17px}
  .role-text{position:absolute;left:77px;font-size:15px;line-height:19px;color:var(--ink)}
  .write-line{position:absolute;left:462px;width:256px;border-bottom:2px dotted #b5b5b5}

  .steps{position:absolute;left:90px;list-style:none;font-size:15.5px;color:var(--ink)}
  .steps li{position:relative;padding-left:22px;height:31px;line-height:20px}
  .steps li::before{content:"";position:absolute;left:0;top:1px;border-left:12px solid var(--orange);
    border-top:9px solid transparent;border-bottom:9px solid transparent}
</style>
</head>
<body>
<main class="sheet">

  <header class="step-banner">
    <div class="step-badge"></div>
    <div class="step-number">5</div>
    <h1 class="step-title">Launch the Project</h1>
  </header>

  <h2 class="tag" style="top:130px">The Who’s Who?</h2>

  <section class="intro">
    <p>These are positions that are played in any project or business.</p>
    <ul>
      <li>Read each description.</li>
      <li>Match each of your group members (including you) with the position that fits best!</li>
    </ul>
  </section>

  <article class="role" style="top:285px">
    <svg class="role-icon" viewBox="0 0 66 66" role="img" aria-label="Icon of a speaking person">
      <circle cx="33" cy="38" r="28" fill="none" stroke="#f7a229" stroke-width="5"/>
      <circle cx="33" cy="42" r="17" fill="#8a8a8a" opacity=".55"/>
      <circle cx="45" cy="13" r="10" fill="#fff" stroke="#f7a229" stroke-width="3"/>
    </svg>
    <h3 class="role-head" style="top:7px"><span class="role-name">THE GO-GETTERS</span><span class="role-area">Public relations and sales</span></h3>
    <p class="role-text" style="top:40px">These people like to talk and get people’s attention.<br>&nbsp;“Why be shy?” They promote and sell.</p>
    <div class="write-line" style="top:66px"></div>
  </article>

  <article class="role" style="top:397px">
    <svg class="role-icon" viewBox="0 0 66 66" aria-hidden="true">
      <circle cx="33" cy="33" r="28" fill="#fff" stroke="#f7a229" stroke-width="5"/>
      <g stroke="#e4e4e4" stroke-width="1">
        <path d="M14 20H52M14 27H52M14 34H52M14 41H52M14 48H52M20 14V54M27 14V54M34 14V54M41 14V54M48 14V54"/>
      </g>
      <polyline points="10,44 20,36 25,40 32,30 37,36 54,27" fill="none" stroke="#f26b3a" stroke-width="2"/>
    </svg>
    <h3 class="role-head" style="top:0"><span class="role-name">THE NUMBER-CRUNCHERS</span><span class="role-area">Finance and Administration</span></h3>
    <p class="role-text" style="top:33px">These people are organized and can keep track of<br>money and information.</p>
    <div class="write-line" style="top:61px"></div>
  </article>

  <article class="role" style="top:507px">
    <svg class="role-icon" viewBox="0 0 66 66" aria-hidden="true">
      <circle cx="33" cy="33" r="28" fill="#fff" stroke="#f7a229" stroke-width="5"/>
      <g fill="#606060">
        <circle cx="33" cy="33" r="14"/>
        <rect x="29" y="13" width="8" height="40" rx="1"/>
        <rect x="13" y="29" width="40" height="8" rx="1"/>
        <rect x="29" y="13" width="8" height="40" rx="1" transform="rotate(45 33 33)"/>
        <rect x="29" y="13" width="8" height="40" rx="1" transform="rotate(-45 33 33)"/>
      </g>
      <circle cx="33" cy="33" r="6" fill="#fff"/>
    </svg>
    <h3 class="role-head" style="top:2px"><span class="role-name">THE DOERS</span><span class="role-area">Production or Service provider</span></h3>
    <p class="role-text" style="top:35px;line-height:22px">If it’s a product- they’ll make it.<br>If it’s a service- they’ll provide it. You can count on them!</p>
    <div class="write-line" style="top:67px"></div>
  </article>

  <article class="role" style="top:616px">
    <svg class="role-icon" viewBox="0 0 66 66" role="img" aria-label="Icon of a person holding a sign">
      <circle cx="33" cy="33" r="28" fill="#fff" stroke="#f7a229" stroke-width="5"/>
      <rect x="15" y="16" width="36" height="36" rx="4" fill="#f26b3a" opacity=".7"/>
    </svg>
    <h3 class="role-head" style="top:2px"><span class="role-name">THE MAGICIANS</span><span class="role-area">Advertising and Publicity</span></h3>
    <p class="role-text" style="top:35px">They have creative ideas.&nbsp; They come up with cool<br>advertisements, slogans, and posters.</p>
    <div class="write-line" style="top:62px"></div>
  </article>

  <article class="role" style="top:729px">
    <svg class="role-icon" viewBox="0 0 66 66" aria-hidden="true">
      <circle cx="33" cy="33" r="28" fill="#fff" stroke="#f7a229" stroke-width="5"/>
      <path d="M6 33Q33 8 60 33Q33 58 6 33Z" fill="#f7a229"/>
      <circle cx="33" cy="33" r="14" fill="#c9c9c9"/>
      <circle cx="33" cy="33" r="5" fill="#555"/>
    </svg>
    <h3 class="role-head" style="top:0"><span class="role-name">THE CHAMELEON</span><span class="role-area">Project manager</span></h3>
    <p class="role-text" style="top:33px">They keep track of everything that needs to be done<br>and who needs to do it!</p>
    <div class="write-line" style="top:61px"></div>
  </article>

  <h2 class="tag" style="top:845px">Go</h2>
  <ul class="steps" style="top:893px">
    <li>You have a great project idea.</li>
    <li style="height:38px">Now make it happen.</li>
    <li>Your idea will probably change.</li>
    <li>Just keep moving forward.</li>
  </ul>

  <h2 class="tag" style="top:1041px">The G-Pack</h2>
  <ul class="steps" style="top:1090px">
    <li>Use the tools in it to help you.</li>
  </ul>

</main>
</body>
</html>
```